Kalvendor Whitmane & Associates

We would like a simple, professional business card using a similar font to our logo.

Industry/Entity Type

Law Firm

Contact Information for Business Card

Martin Kalvendor, Esq. 48 Fennimore Lane, 2nd Floor Larkhaven, VT 04173 Office: 555.216.4093 Cell: 555.370.8154 Email: marty@kwlawfirm.example kalvendorwhitmanelaw.example

Font styles to use
Other font styles liked:
• We would like to use the fonts used in the logo or similar

Colors
0054AA
0677BA
7BADD7
CADEEF
E8F1F8

Requirements
Must have
• We would like the fonts to match the logo
Nice to have
• not too much design- very simple and professional business card. I added a picture of a business card that I tried to start but I am not a designer! Hopefully it will help with the address and phone numbers and kind of what we are looking for.

```html
<!DOCTYPE html>
<html lang="en">
<head>
<meta charset="utf-8">
<title>Kalvendor Whitmane &amp; Associates – Business Card</title>
<link rel="stylesheet" href="https://fonts.googleapis.com/css2?family=Cinzel:wght@600&family=Crimson+Pro:wght@700&family=Manrope:wght@400;700&display=swap">
<style>
  :root {
    --navy: #2b3f7a;
    --navy-deep: #24366c;
    --paper: #ffffff;
    --stage: #e9eaec;
    --ink-grey: #6b6e74;
    --rule: #2b3f7a;
  }
  * { margin: 0; padding: 0; box-sizing: border-box; }
  html, body {
    width: 1200px; height: 794px; overflow: hidden;
    background: var(--stage);
  }
  .stage { position: relative; width: 1200px; height: 794px; }

  .card {
    position: absolute;
    width: 520px; height: 297px;
    border-radius: 3px;
    box-shadow: 0 2px 6px rgba(0,0,0,0.12);
    overflow: hidden;
  }

  /* Back of card */
  .card-back {
    left: 90px; top: 100px;
    background: var(--navy);
    display: flex; align-items: center; justify-content: center;
  }

  /* Firm name lockup: one colour, one weight */
  .firm { display: flex; align-items: center; gap: 16px; }
  .firm-square { width: 34px; height: 34px; flex: none; }
  .firm-name {
    font-family: "Cinzel", serif;
    font-weight: 600;
    line-height: 1.05;
    letter-spacing: 0.02em;
    text-align: left;
  }
  .firm-name span { display: block; }
  .card-back .firm-square { background: var(--paper); }
  .card-back .firm-name { color: var(--paper); font-size: 24px; }

  /* Front of card */
  .card-front {
    left: 590px; top: 400px;
    background: var(--paper);
    text-align: center;
    padding-top: 34px;
  }
  .card-front::after {
    content: ""; position: absolute; left: 0; right: 0; bottom: 0;
    height: 9px; background: var(--navy);
  }
  .card-front .firm { justify-content: center; }
  .card-front .firm-square { background: var(--navy); width: 28px; height: 28px; }
  .card-front .firm-name { color: var(--navy); font-size: 19px; }

  .holder {
    margin-top: 22px;
    font-family: "Crimson Pro", serif;
    font-weight: 700;
    font-size: 21px;
    color: var(--navy-deep);
    letter-spacing: 0.04em;
  }
  .holder-rule {
    width: 56px; height: 1.5px; background: var(--rule);
    margin: 8px auto 12px;
  }
  .contact {
    font-family: "Manrope", sans-serif;
    font-size: 12px;
    color: var(--ink-grey);
    line-height: 1.6;
  }
  .contact .label {
    font-weight: 700; color: var(--navy);
    font-size: 10px; letter-spacing: 0.06em; text-transform: uppercase;
    margin-right: 3px;
  }
  .contact .item + .item { margin-left: 8px; }
  .website {
    font-family: "Manrope", sans-serif;
    font-weight: 700; font-size: 13.5px;
    color: var(--navy); margin-top: 2px;
  }
</style>
</head>
<body>
<main class="stage">
  <section class="card card-back" aria-label="Card back">
    <div class="firm">
      <div class="firm-square"></div>
      <div class="firm-name"><span>Kalvendor</span><span>Whitmane</span><span>&amp; Associates</span></div>
    </div>
  </section>

  <section class="card card-front" aria-label="Card front">
    <div class="firm">
      <div class="firm-square"></div>
      <div class="firm-name"><span>Kalvendor</span><span>Whitmane</span><span>&amp; Associates</span></div>
    </div>
    <p class="holder">MARTIN KALVENDOR, Esq.</p>
    <div class="holder-rule"></div>
    <div class="contact">
      <p>
        <span class="item"><span class="label">Office</span>555.216.4093</span>
        <span class="item"><span class="label">Cell</span>555.370.8154</span>
        <span class="item"><span class="label">Email</span>marty@kwlawfirm.example</span>
      </p>
      <p>48 Fennimore Lane, 2nd Floor, Larkhaven, VT 04173</p>
    </div>
    <p class="website">kalvendorwhitmanelaw.example</p>
  </section>
</main>
</body>
</html>
```